Supplement label for Brain health

I need a design for a supplement this supplement is a brain boost supplement.

The Name is Kelp Vantor.

I have attached other labels I like. This is for 50 plus demographic so the lettering needs to be easy to read and stand out. I have attached a dummy label template that once the winner is choosen then they will get the real supplement facts etc.

Clean desgin easy to read.

This file must be finished in AI format.

Target Market(s)

50 plus 70 percent female 30 percent male

Industry/Entity Type

Supplement

Font styles to use
Other font styles liked:
• Myrid pro maybe

Requirements
Must have
• easy to read text so no colors that hide text or hard to read.

```html
<!DOCTYPE html>
<html lang="en">
<head>
<meta charset="utf-8">
<title>Kelp Vantor Brain Booster Label</title>
<link href="https://fonts.googleapis.com/css2?family=Oswald:wght@600&family=PT+Sans:wght@400;700&display=swap" rel="stylesheet">
<style>
  :root {
    --page-bg: #eceef0;
    --navy: #0d1f5e;
    --navy-deep: #0a1748;
    --glow: #4f8fd9;
    --orange: #de7a0e;
    --white: #ffffff;
    --ink: #1b2f6e;
  }
  html, body {
    margin: 0;
    padding: 0;
    width: 1200px;
    height: 1200px;
    overflow: hidden;
    background: var(--page-bg);
  }
  .label {
    position: absolute;
    left: 100px;
    top: 34px;
    width: 1000px;
    height: 1132px;
    background: var(--white);
    overflow: hidden;
    box-shadow: 0 2px 10px rgba(0,0,0,0.08);
  }
  .hero {
    position: absolute;
    left: 0;
    top: 0;
    width: 1000px;
    height: 832px;
    background: linear-gradient(160deg, var(--navy-deep) 0%, var(--navy) 60%, #132a72 100%);
  }
  .hero-art {
    position: absolute;
    left: 300px;
    top: 0;
    width: 700px;
    height: 832px;
    background:
      radial-gradient(ellipse 40% 30% at 58% 28%, rgba(150,200,255,0.55), transparent 70%),
      radial-gradient(ellipse 55% 60% at 55% 55%, rgba(79,143,217,0.45), transparent 75%),
      radial-gradient(ellipse 50% 25% at 20% 12%, rgba(160,200,255,0.25), transparent 70%);
  }
  .brand-banner {
    position: absolute;
    left: 0;
    top: 0;
    width: 1000px;
    height: 240px;
  }
  .brand-name {
    position: absolute;
    left: 100px;
    top: 66px;
    margin: 0;
    font-family: "PT Sans", sans-serif;
    font-weight: 400;
    font-size: 46px;
    color: var(--white);
    letter-spacing: 0.5px;
  }
  .product-title {
    position: absolute;
    left: 74px;
    top: 440px;
    margin: 0;
    font-family: "Oswald", sans-serif;
    font-weight: 600;
    font-size: 172px;
    line-height: 186px;
    color: var(--white);
    text-transform: uppercase;
    letter-spacing: -1px;
  }
  .type-band {
    position: absolute;
    left: 0;
    top: 832px;
    width: 1000px;
    height: 104px;
    background: var(--orange);
  }
  .type-band span {
    position: absolute;
    left: 77px;
    top: 12px;
    font-family: "PT Sans", sans-serif;
    font-weight: 400;
    font-size: 78px;
    line-height: 80px;
    color: var(--navy);
    letter-spacing: 1px;
  }
  .claim {
    position: absolute;
    left: 77px;
    top: 955px;
    margin: 0;
    font-family: "PT Sans", sans-serif;
    font-weight: 700;
    font-size: 58px;
    color: var(--ink);
  }
  .footer-line {
    position: absolute;
    left: 77px;
    right: 38px;
    top: 1050px;
    display: flex;
    justify-content: space-between;
    font-family: "PT Sans", sans-serif;
    font-weight: 700;
    font-size: 33px;
    color: var(--ink);
    text-transform: uppercase;
  }
</style>
</head>
<body>
  <div class="label">
    <div class="hero">
      <div class="hero-art" role="img" aria-label="Glowing blue illustration of a human head in profile with a luminous brain and neural light trails"></div>
      <svg class="brand-banner" viewBox="0 0 1000 240" aria-hidden="true">
        <polyline points="77,0 77,227 276,160 480,227 480,0" fill="none" stroke="#ffffff" stroke-width="3"/>
        <line x1="480" y1="80" x2="1000" y2="80" stroke="#ffffff" stroke-width="2.5"/>
      </svg>
      <p class="brand-name">Kelp Vantor</p>
      <h1 class="product-title">Brain<br>Booster</h1>
    </div>
    <div class="type-band"><span>SUPPLEMENT</span></div>
    <p class="claim">Promotes Brain function*</p>
    <div class="footer-line">
      <span>Dietary Supplement</span>
      <span>30 Capsules</span>
    </div>
  </div>
</body>
</html>
```